The house buying company website creation

A slick professional landing page it needs to be a very engaging custom designed landing page.

It must have a lead generation tool/box similar to my competitors that will recognise the address when they start to enter the address or postcode.

My main competitors websites to use ideas from to build trust and look correct are: www.brindlemarsh.com quorvahomes.com

Target Market(s)

People looking to sell their house or property fast. We will buy their property

Industry/Entity Type

Real Estate

Coding

Coded - Design and coding required

Number of Pages Required

1 page

Requirements
Must have
• A lead generation tool that is similar to my competitors to gather their essential details. (please check www.quorvahomes.com or www.brindlemarsh.com to see what i want.

It also must have all the aspects my competitors has on their landing page. All companies in this industry have this on the landing page. These include: Logos to build trust. Ours can be The Vellmoor Logo, the seen on TV logo, The Harrowgate Ledger online logo. Also we need a step by step process map to show the customer how it works.

If the customer is about to leave the page it Must have flash ups that ask the customer to fill in 4 boxes. first name, surname, email, Phone number and address. Check out quorvahomes.com to see what i want.

must have a comparison table similar to my competitors. I can include this on the draft.

Must have my frequently asked questions for google SEO ( I will upload these to here to the winner to add this page at the end.

It must be a slick professional design that tells people they are dealing with a company they can trust who has the funds on hand to purchase hundreds of property.
Nice to have
• It must be a slick professional design that tells people they are dealing with a company they can trust who has the funds on hand to purchase hundreds of property.
Should not have
• Anything cheap or tacky looking.

```html
<!DOCTYPE html>
<html lang="en">
<head>
<meta charset="utf-8">
<title>Hearthway Homes – Sell your house fast</title>
<link rel="stylesheet" href="https://fonts.googleapis.com/css2?family=Open+Sans:wght@400;600;700;800&display=swap">
<style>
:root{
  --stage:#d6d7d9;
  --green:#3fae49;
  --green-dark:#2e8f3a;
  --navy:#2c3a4f;
  --navy-deep:#222e40;
  --ink:#2f3440;
  --muted:#8a909a;
  --line:#e3e6ea;
  --soft:#f3f5f7;
  --white:#ffffff;
  --red:#e05a4f;
  --shade:rgba(20,28,40,.72);
}
*{box-sizing:border-box;margin:0;padding:0}
html,body{width:1200px;height:2580px;overflow:hidden}
body{background:var(--stage);font-family:"Open Sans",Arial,sans-serif;color:var(--ink);position:relative}
.page{position:absolute;top:100px;width:532px;height:2428px;background:var(--white);overflow:hidden;box-shadow:0 4px 18px rgba(0,0,0,.12)}
.page--main{left:60px}
.page--exit{left:632px}
.section{position:relative;text-align:center}
.kicker{font-size:6px;color:var(--green);font-weight:700;letter-spacing:.5px;text-transform:uppercase}
.title{font-size:15px;font-weight:800;color:var(--ink)}
.title em{font-style:normal;color:var(--green)}
.small{font-size:6px;line-height:1.6;color:var(--muted)}
.btn{display:inline-block;background:var(--green);color:var(--white);font-size:6.5px;font-weight:700;padding:5px 12px;border-radius:3px}

/* header */
.header{height:60px;display:flex;align-items:center;justify-content:space-between;padding:0 22px}
.header__phone{font-size:6px;color:var(--muted);text-align:left;line-height:1.4}
.header__phone b{display:block;font-size:8px;color:var(--navy)}
.brand{display:flex;flex-direction:column;align-items:center;gap:3px}
.brand__dot{width:18px;height:18px;border-radius:50%;background:var(--green)}
.brand__name{font-size:7px;font-weight:700;color:var(--green)}
.nav{position:absolute;left:22px;right:22px;bottom:2px;display:flex;justify-content:space-between;font-size:5px;color:var(--muted)}

/* hero */
.hero{height:240px;overflow:hidden}
.hero__photo{position:absolute;inset:0;background:linear-gradient(180deg,#5d6b58 0%,#7a8a6b 45%,#95a283 100%)}
.hero__shade{position:absolute;inset:0;background:rgba(30,40,50,.35)}
.hero__content{position:relative;padding-top:46px;color:var(--white)}
.hero__title{font-size:17px;font-weight:800;line-height:1.25}
.hero__sub{font-size:7px;margin-top:6px;opacity:.9}
.hero__form{display:flex;justify-content:center;margin-top:16px}
.hero__input{width:190px;height:20px;background:var(--white);border-radius:3px 0 0 3px;font-size:6px;color:var(--muted);text-align:left;padding:6px 8px}
.hero__form .btn{border-radius:0 3px 3px 0;padding:6px 12px}
.hero__note{font-size:5.5px;margin-top:8px;opacity:.85}
.hero__curve{position:absolute;left:0;bottom:0;width:532px;height:40px}

/* press */
.press{height:56px;display:flex;align-items:center;justify-content:space-around;padding:0 30px;border-bottom:1px solid var(--line)}
.press__label{font-size:8px;font-weight:700;color:var(--ink)}
.press__name{font-size:8px;font-weight:700;color:var(--ink)}
.press__badge{width:22px;height:16px;background:var(--red);border-radius:3px}

/* steps */
.how{height:300px;padding-top:40px}
.steps{display:flex;justify-content:center;gap:44px;margin-top:22px}
.step{width:100px}
.step__photo{position:relative;width:64px;height:64px;margin:0 auto;border-radius:50%;background:radial-gradient(circle,#c9c3b8,#8d8779);border:3px solid var(--white);box-shadow:0 0 0 2px var(--line)}
.step__icon{position:absolute;left:-6px;bottom:2px;width:20px;height:20px;border-radius:50%;background:var(--green);display:flex;align-items:center;justify-content:center}
.step__title{font-size:7px;font-weight:700;margin-top:10px}
.step .small{margin-top:4px}

/* quick */
.quick{height:300px;background:var(--soft);padding-top:22px}
.quick__body{display:flex;gap:18px;padding:18px 60px 0;text-align:left;align-items:center}
.quick__photo{width:200px;height:120px;background:linear-gradient(135deg,#c7bba7,#8c7e69);border-radius:2px;flex-shrink:0}
.quick__bar{position:absolute;left:0;right:0;bottom:0;height:74px;background:var(--navy);display:flex;align-items:center;justify-content:space-between;padding:0 40px;color:var(--white)}
.quick__bar h3{font-size:11px;font-weight:700}
.quick__bar h3 em{font-style:normal;color:var(--green)}
.quick__field{display:flex}
.quick__input{width:150px;height:18px;background:var(--white);border-radius:3px 0 0 3px;font-size:5.5px;color:var(--muted);padding:5px 6px;text-align:left}
.quick__field .btn{border-radius:0 3px 3px 0}

/* types */
.types{height:250px;padding-top:30px}
.types__grid{display:grid;grid-template-columns:repeat(3,1fr);gap:18px 18px;padding:22px 70px 0;text-align:left}
.type{display:flex;gap:7px;align-items:flex-start}
.type__icon{width:18px;height:18px;border-radius:50%;background:var(--green);flex-shrink:0;display:flex;align-items:center;justify-content:center}
.type b{display:block;font-size:6px;color:var(--ink)}
.type span{font-size:5px;color:var(--muted);line-height:1.5;display:block}

/* compare */
.compare{height:350px;background:var(--soft);padding-top:30px}
.table{width:380px;margin:18px auto 0;border-collapse:collapse;font-size:5.5px;background:var(--white)}
.table th{background:var(--navy);color:var(--white);padding:6px;font-weight:700}
.table th.us{background:var(--green)}
.table td{padding:5px 6px;border-bottom:1px solid var(--line);text-align:center;color:var(--ink)}
.table td:first-child{text-align:left}
.table tr.hl td{background:#e6f4e7}
.yes{color:var(--green);font-weight:800}
.no{color:var(--red);font-weight:800}
.compare__note{font-size:6px;color:var(--muted);margin-top:10px}

/* reviews */
.reviews{height:230px;background:var(--green);padding-top:36px;color:var(--white)}
.reviews .title{color:var(--white)}
.reviews__row{display:flex;gap:26px;padding:26px 50px 0;text-align:left}
.review{flex:1}
.review__quote{font-size:14px;font-weight:800;line-height:1}
.review p{font-size:5.5px;line-height:1.6;opacity:.9;margin-top:4px}
.review__who{display:flex;align-items:center;gap:5px;margin-top:8px;font-size:5.5px;font-weight:700}
.review__who i{width:12px;height:12px;border-radius:50%;background:rgba(255,255,255,.45);display:block}

/* why */
.why{height:210px;display:flex;padding:34px 50px 0;gap:30px;text-align:left}
.why__list{flex:1}
.why__item{display:flex;gap:6px;margin-top:10px}
.why__item i{width:12px;height:12px;border-radius:50%;background:var(--green);flex-shrink:0;display:block}
.why__item b{font-size:6px;display:block}
.why__photo{width:170px;height:120px;background:linear-gradient(135deg,#d9cfc2,#9a8c7a);margin-top:6px}

/* recent */
.recent{height:220px;padding-top:24px}
.recent__row{display:flex;gap:10px;padding:18px 50px 0}
.house{flex:1;height:96px;background:linear-gradient(180deg,#b9c6cf 0%,#a0765e 55%,#6f5f4d 100%)}
.house:nth-child(2){background:linear-gradient(180deg,#c0cbd3 0%,#b58a6b 55%,#5d6a52 100%)}
.house:nth-child(3){background:linear-gradient(180deg,#bcc8d1 0%,#94694f 55%,#6b6b5a 100%)}
.house:nth-child(4){background:linear-gradient(180deg,#c6d0d6 0%,#a98066 55%,#667058 100%)}
.recent__arrows{position:absolute;right:50px;top:28px;display:flex;gap:4px}
.recent__arrows i{width:12px;height:12px;border:1px solid var(--line);border-radius:2px;display:block}

/* footer */
.footer{height:212px;color:var(--white)}
.footer__bg{position:absolute;left:0;top:0;width:532px;height:212px}
.footer__cols{position:relative;display:flex;gap:34px;padding:58px 40px 0;text-align:left}
.footer__brand{width:110px;text-align:center}
.footer__brand .brand__name{color:var(--white);margin-top:4px}
.footer__social{display:flex;justify-content:center;gap:4px;margin-top:8px}
.footer__social i{width:10px;height:10px;border-radius:50%;border:1px solid rgba(255,255,255,.6);display:block}
.footer__col h4{font-size:6.5px;font-weight:700;margin-bottom:6px}
.footer__col p{font-size:5.5px;line-height:1.9;opacity:.75}
.footer__legal{position:absolute;left:0;right:0;bottom:12px;font-size:5px;opacity:.6}

/* exit-intent overlay */
.overlay{position:absolute;inset:0;background:var(--shade)}
.popup{position:absolute;left:160px;top:22px;width:212px;background:var(--navy-deep);border:1px solid rgba(255,255,255,.15);border-radius:3px;padding:14px 16px 16px;color:var(--white);text-align:center}
.popup h3{font-size:8.5px;font-weight:700}
.popup p{font-size:5.5px;opacity:.75;margin-top:3px}
.popup__field{height:18px;background:var(--white);border-radius:2px;margin-top:7px;font-size:5.5px;color:var(--muted);text-align:left;padding:5px 6px}
.popup .btn{margin-top:10px;padding:5px 22px}
</style>
</head>
<body>

<!-- MAIN PAGE -->
<main class="page page--main">
  <header class="section header">
    <div class="header__phone">Call us free<b>0800 555 0192</b></div>
    <div class="brand"><span class="brand__dot"></span><span class="brand__name">Hearthway Homes</span></div>
    <span class="btn">Get a cash offer</span>
    <nav class="nav"><span>How it works</span><span>Why sell to us</span><span>Reviews</span><span>Recent sales</span><span>FAQs</span><span>Contact</span></nav>
  </header>

  <section class="section hero">
    <div class="hero__photo" role="img" aria-label="Aerial view of a residential street with rows of houses and trees"></div>
    <div class="hero__shade"></div>
    <div class="hero__content">
      <h1 class="hero__title">We will buy any type of property fast</h1>
      <p class="hero__sub">Get a free, no-obligation cash offer in 24 hours</p>
      <div class="hero__form"><div class="hero__input">Enter your postcode or address</div><span class="btn">Get my offer</span></div>
      <p class="hero__note">No fees · No obligation · Completion in as little as 7 days</p>
    </div>
    <svg class="hero__curve" viewBox="0 0 532 40" preserveAspectRatio="none"><path d="M0 18 Q266 52 532 18 L532 40 L0 40Z" fill="#fff"/><path d="M0 18 Q266 52 532 18" fill="none" stroke="#3fae49" stroke-width="2"/></svg>
  </section>

  <section class="section press">
    <span class="press__label">Featured in...</span>
    <span class="press__name">The Vellmoor</span>
    <span class="press__badge"></span>
    <span class="press__name">The Harrowgate Ledger online</span>
  </section>

  <section class="section how">
    <p class="kicker">Simple process</p>
    <h2 class="title">How it <em>Works</em></h2>
    <div class="steps">
      <div class="step"><div class="step__photo" role="img" aria-label="Person entering address on a laptop"><span class="step__icon"><svg width="10" height="10" viewBox="0 0 10 10"><path d="M5 1 L9 5 H8 V9 H2 V5 H1Z" fill="#fff"/></svg></span></div><p class="step__title">1. Enter your details</p><p class="small">Tell us about your home in under two minutes online.</p></div>
      <div class="step"><div class="step__photo" role="img" aria-label="Adviser on the phone making an offer"><span class="step__icon"><svg width="10" height="10" viewBox="0 0 10 10"><path d="M2 1 L4 1 L5 3 L4 4 Q5 6 6 6 L7 5 L9 6 L9 8 Q5 9 1 3Z" fill="#fff"/></svg></span></div><p class="step__title">2. Get a cash offer</p><p class="small">We make a fair cash offer within 24 hours.</p></div>
      <div class="step"><div class="step__photo" role="img" aria-label="Keys being handed over at a front door"><span class="step__icon"><svg width="10" height="10" viewBox="0 0 10 10"><path d="M2 5 L4 7 L8 3" stroke="#fff" stroke-width="1.6" fill="none"/></svg></span></div><p class="step__title">3. Complete the sale</p><p class="small">Pick your completion date and get paid fast.</p></div>
    </div>
  </section>

  <section class="section quick">
    <p class="kicker">Fast completion</p>
    <h2 class="title">How quickly can we buy your house?</h2>
    <div class="quick__body">
      <div class="quick__photo" role="img" aria-label="Couple relaxing on a sofa in their living room"></div>
      <p class="small">We have cash funds ready, so we can complete in as little as seven days. No chains, no surveys falling through and no waiting for buyer mortgages. You choose the date that suits you best.</p>
    </div>
    <div class="quick__bar"><h3>Get your <em>cash offer</em> today</h3><div class="quick__field"><div class="quick__input">Enter your postcode</div><span class="btn">Get offer</span></div></div>
  </section>

  <section class="section types">
    <h2 class="title">We buy all types of <em>property</em></h2>
    <div class="types__grid">
      <div class="type"><span class="type__icon"><svg width="9" height="9" viewBox="0 0 10 10"><path d="M5 1 L9 5 H8 V9 H2 V5 H1Z" fill="#fff"/></svg></span><div><b>Houses</b><span>Detached, semi and terraced homes</span></div></div>
      <div class="type"><span class="type__icon"><svg width="9" height="9" viewBox="0 0 10 10"><path d="M5 1 L9 5 H8 V9 H2 V5 H1Z" fill="#fff"/></svg></span><div><b>Flats</b><span>Any floor, leasehold or share</span></div></div>
      <div class="type"><span class="type__icon"><svg width="9" height="9" viewBox="0 0 10 10"><path d="M5 1 L9 5 H8 V9 H2 V5 H1Z" fill="#fff"/></svg></span><div><b>Bungalows</b><span>Single storey homes of any size</span></div></div>
      <div class="type"><span class="type__icon"><svg width="9" height="9" viewBox="0 0 10 10"><path d="M5 1 L9 5 H8 V9 H2 V5 H1Z" fill="#fff"/></svg></span><div><b>Probate</b><span>Inherited homes sold with care</span></div></div>
      <div class="type"><span class="type__icon"><svg width="9" height="9" viewBox="0 0 10 10"><path d="M5 1 L9 5 H8 V9 H2 V5 H1Z" fill="#fff"/></svg></span><div><b>Repossession</b><span>Stop arrears and sell quickly</span></div></div>
      <div class="type"><span class="type__icon"><svg width="9" height="9" viewBox="0 0 10 10"><path d="M5 1 L9 5 H8 V9 H2 V5 H1Z" fill="#fff"/></svg></span><div><b>Tenanted</b><span>Buy-to-let with tenants in place</span></div></div>
      <div class="type"><span class="type__icon"><svg width="9" height="9" viewBox="0 0 10 10"><path d="M5 1 L9 5 H8 V9 H2 V5 H1Z" fill="#fff"/></svg></span><div><b>Needs repair</b><span>Any condition, no work needed</span></div></div>
      <div class="type"><span class="type__icon"><svg width="9" height="9" viewBox="0 0 10 10"><path d="M5 1 L9 5 H8 V9 H2 V5 H1Z" fill="#fff"/></svg></span><div><b>Divorce</b><span>A clean, quick and fair split</span></div></div>
      <div class="type"><span class="type__icon"><svg width="9" height="9" viewBox="0 0 10 10"><path d="M5 1 L9 5 H8 V9 H2 V5 H1Z" fill="#fff"/></svg></span><div><b>Short lease</b><span>Low lease years are no problem</span></div></div>
    </div>
  </section>

  <section class="section compare">
    <h2 class="title">Why sell your property to <em>Hearthway Homes</em></h2>
    <table class="table">
      <tr><th>Feature</th><th class="us">Hearthway Homes</th><th>Estate agent</th><th>Auction</th></tr>
      <tr class="hl"><td>Guaranteed sale</td><td class="yes">✓</td><td class="no">✕</td><td class="no">✕</td></tr>
      <tr><td>Sale time</td><td>7 days</td><td>6 months</td><td>3 months</td></tr>
      <tr><td>Agent fees</td><td class="yes">✓ None</td><td>1–3%</td><td>2–5%</td></tr>
      <tr><td>Legal fees paid</td><td class="yes">✓</td><td class="no">✕</td><td class="no">✕</td></tr>
      <tr><td>No viewings</td><td class="yes">✓</td><td class="no">✕</td><td class="no">✕</td></tr>
      <tr><td>Chain free</td><td class="yes">✓</td><td class="no">✕</td><td class="yes">✓</td></tr>
      <tr><td>Choose completion date</td><td class="yes">✓</td><td class="no">✕</td><td class="no">✕</td></tr>
      <tr><td>Any condition</td><td class="yes">✓</td><td class="no">✕</td><td class="yes">✓</td></tr>
    </table>
    <p class="compare__note">Cash funds ready to purchase hundreds of properties</p>
  </section>

  <section class="section reviews">
    <h2 class="title">Happy Customers</h2>
    <div class="reviews__row">
      <div class="review"><div class="review__quote">“</div><p>Fast, fair and honest. We sold in under two weeks without any stress at all.</p><div class="review__who"><i></i>Sarah M.</div></div>
      <div class="review"><div class="review__quote">“</div><p>The offer was clear and they kept every promise. Highly recommended team.</p><div class="review__who"><i></i>David R.</div></div>
      <div class="review"><div class="review__quote">“</div><p>We needed to move quickly and they made the whole process simple.</p><div class="review__who"><i></i>Karen T.</div></div>
    </div>
  </section>

  <section class="section why">
    <div class="why__list">
      <h2 class="title">Why Choose Us</h2>
      <p class="small">A trusted cash buyer with funds on hand.</p>
      <div class="why__item"><i></i><div><b>Cash ready to buy</b><span class="small">No mortgages or chains involved.</span></div></div>
      <div class="why__item"><i></i><div><b>No hidden fees</b><span class="small">We cover all legal costs for you.</span></div></div>
      <div class="why__item"><i></i><div><b>Your timescale</b><span class="small">Complete on the date you choose.</span></div></div>
    </div>
    <div class="why__photo" role="img" aria-label="Couple carrying moving boxes into a new home"></div>
  </section>

  <section class="section recent">
    <h2 class="title">Recent sales <em>Anfield</em></h2>
    <div class="recent__arrows"><i></i><i></i></div>
    <div class="recent__row">
      <div class="house" role="img" aria-label="Brick terraced house recently bought"></div>
      <div class="house" role="img" aria-label="Semi-detached house recently bought"></div>
      <div class="house" role="img" aria-label="Red brick end-terrace house recently bought"></div>
      <div class="house" role="img" aria-label="Detached family house recently bought"></div>
    </div>
  </section>

  <footer class="section footer">
    <svg class="footer__bg" viewBox="0 0 532 212" preserveAspectRatio="none"><path d="M0 30 Q266 -10 532 30 L532 212 L0 212Z" fill="#2c3a4f"/><path d="M0 30 Q266 -10 532 30" fill="none" stroke="#3fae49" stroke-width="2"/></svg>
    <div class="footer__cols">
      <div class="footer__brand"><div class="brand"><span class="brand__dot"></span></div><div class="brand__name">Hearthway Homes</div><div class="footer__social"><i></i><i></i><i></i><i></i></div></div>
      <div class="footer__col"><h4>Company</h4><p>About us<br>How it works<br>Reviews<br>Careers</p></div>
      <div class="footer__col"><h4>Help</h4><p>FAQs<br>Contact<br>Privacy<br>Terms</p></div>
      <div class="footer__col"><h4>Contact</h4><p>0800 555 0192<br>hello@hearthwayhomes.com<br>Mon–Sat 8am–8pm</p></div>
    </div>
    <p class="footer__legal">© Hearthway Homes. All rights reserved.</p>
  </footer>
</main>

<!-- EXIT-INTENT STATE -->
<main class="page page--exit">
  <header class="section header">
    <div class="header__phone">Call us free<b>0800 555 0192</b></div>
    <div class="brand"><span class="brand__dot"></span><span class="brand__name">Hearthway Homes</span></div>
    <span class="btn">Get a cash offer</span>
    <nav class="nav"><span>How it works</span><span>Why sell to us</span><span>Reviews</span><span>Recent sales</span><span>FAQs</span><span>Contact</span></nav>
  </header>

  <section class="section hero">
    <div class="hero__photo" role="img" aria-label="Aerial view of a residential street with rows of houses and trees"></div>
    <div class="hero__shade"></div>
    <svg class="hero__curve" viewBox="0 0 532 40" preserveAspectRatio="none"><path d="M0 18 Q266 52 532 18 L532 40 L0 40Z" fill="#fff"/><path d="M0 18 Q266 52 532 18" fill="none" stroke="#3fae49" stroke-width="2"/></svg>
  </section>

  <section class="section press">
    <span class="press__label">Featured in...</span>
    <span class="press__name">The Vellmoor</span>
    <span class="press__badge"></span>
    <span class="press__name">The Harrowgate Ledger online</span>
  </section>

  <section class="section how">
    <p class="kicker">Simple process</p>
    <h2 class="title">How it <em>Works</em></h2>
    <div class="steps">
      <div class="step"><div class="step__photo" role="img" aria-label="Person entering address on a laptop"><span class="step__icon"></span></div><p class="step__title">1. Enter your details</p><p class="small">Tell us about your home in under two minutes online.</p></div>
      <div class="step"><div class="step__photo" role="img" aria-label="Adviser on the phone making an offer"><span class="step__icon"></span></div><p class="step__title">2. Get a cash offer</p><p class="small">We make a fair cash offer within 24 hours.</p></div>
      <div class="step"><div class="step__photo" role="img" aria-label="Keys being handed over at a front door"><span class="step__icon"></span></div><p class="step__title">3. Complete the sale</p><p class="small">Pick your completion date and get paid fast.</p></div>
    </div>
  </section>

  <section class="section quick">
    <p class="kicker">Fast completion</p>
    <h2 class="title">How quickly can we buy your house?</h2>
    <div class="quick__body">
      <div class="quick__photo" role="img" aria-label="Couple relaxing on a sofa in their living room"></div>
      <p class="small">We have cash funds ready, so we can complete in as little as seven days. No chains, no surveys falling through and no waiting for buyer mortgages. You choose the date that suits you best.</p>
    </div>
    <div class="quick__bar"><h3>Get your <em>cash offer</em> today</h3><div class="quick__field"><div class="quick__input">Enter your postcode</div><span class="btn">Get offer</span></div></div>
  </section>

  <section class="section types">
    <h2 class="title">We buy all types of <em>property</em></h2>
    <div class="types__grid">
      <div class="type"><span class="type__icon"></span><div><b>Houses</b><span>Detached, semi and terraced homes</span></div></div>
      <div class="type"><span class="type__icon"></span><div><b>Flats</b><span>Any floor, leasehold or share</span></div></div>
      <div class="type"><span class="type__icon"></span><div><b>Bungalows</b><span>Single storey homes of any size</span></div></div>
      <div class="type"><span class="type__icon"></span><div><b>Probate</b><span>Inherited homes sold with care</span></div></div>
      <div class="type"><span class="type__icon"></span><div><b>Repossession</b><span>Stop arrears and sell quickly</span></div></div>
      <div class="type"><span class="type__icon"></span><div><b>Tenanted</b><span>Buy-to-let with tenants in place</span></div></div>
      <div class="type"><span class="type__icon"></span><div><b>Needs repair</b><span>Any condition, no work needed</span></div></div>
      <div class="type"><span class="type__icon"></span><div><b>Divorce</b><span>A clean, quick and fair split</span></div></div>
      <div class="type"><span class="type__icon"></span><div><b>Short lease</b><span>Low lease years are no problem</span></div></div>
    </div>
  </section>

  <section class="section compare">
    <h2 class="title">Why sell your property to <em>Hearthway Homes</em></h2>
    <table class="table">
      <tr><th>Feature</th><th class="us">Hearthway Homes</th><th>Estate agent</th><th>Auction</th></tr>
      <tr class="hl"><td>Guaranteed sale</td><td class="yes">✓</td><td class="no">✕</td><td class="no">✕</td></tr>
      <tr><td>Sale time</td><td>7 days</td><td>6 months</td><td>3 months</td></tr>
      <tr><td>Agent fees</td><td class="yes">✓ None</td><td>1–3%</td><td>2–5%</td></tr>
      <tr><td>Legal fees paid</td><td class="yes">✓</td><td class="no">✕</td><td class="no">✕</td></tr>
      <tr><td>No viewings</td><td class="yes">✓</td><td class="no">✕</td><td class="no">✕</td></tr>
      <tr><td>Chain free</td><td class="yes">✓</td><td class="no">✕</td><td class="yes">✓</td></tr>
      <tr><td>Choose completion date</td><td class="yes">✓</td><td class="no">✕</td><td class="no">✕</td></tr>
      <tr><td>Any condition</td><td class="yes">✓</td><td class="no">✕</td><td class="yes">✓</td></tr>
    </table>
    <p class="compare__note">Cash funds ready to purchase hundreds of properties</p>
  </section>

  <section class="section reviews">
    <h2 class="title">Happy Customers</h2>
    <div class="reviews__row">
      <div class="review"><div class="review__quote">“</div><p>Fast, fair and honest. We sold in under two weeks without any stress at all.</p><div class="review__who"><i></i>Sarah M.</div></div>
      <div class="review"><div class="review__quote">“</div><p>The offer was clear and they kept every promise. Highly recommended team.</p><div class="review__who"><i></i>David R.</div></div>
      <div class="review"><div class="review__quote">“</div><p>We needed to move quickly and they made the whole process simple.</p><div class="review__who"><i></i>Karen T.</div></div>
    </div>
  </section>

  <section class="section why">
    <div class="why__list">
      <h2 class="title">Why Choose Us</h2>
      <p class="small">A trusted cash buyer with funds on hand.</p>
      <div class="why__item"><i></i><div><b>Cash ready to buy</b><span class="small">No mortgages or chains involved.</span></div></div>
      <div class="why__item"><i></i><div><b>No hidden fees</b><span class="small">We cover all legal costs for you.</span></div></div>
      <div class="why__item"><i></i><div><b>Your timescale</b><span class="small">Complete on the date you choose.</span></div></div>
    </div>
    <div class="why__photo" role="img" aria-label="Couple carrying moving boxes into a new home"></div>
  </section>

  <section class="section recent">
    <h2 class="title">Recent sales <em>Anfield</em></h2>
    <div class="recent__arrows"><i></i><i></i></div>
    <div class="recent__row">
      <div class="house" role="img" aria-label="Brick terraced house recently bought"></div>
      <div class="house" role="img" aria-label="Semi-detached house recently bought"></div>
      <div class="house" role="img" aria-label="Red brick end-terrace house recently bought"></div>
      <div class="house" role="img" aria-label="Detached family house recently bought"></div>
    </div>
  </section>

  <footer class="section footer">
    <svg class="footer__bg" viewBox="0 0 532 212" preserveAspectRatio="none"><path d="M0 30 Q266 -10 532 30 L532 212 L0 212Z" fill="#2c3a4f"/><path d="M0 30 Q266 -10 532 30" fill="none" stroke="#3fae49" stroke-width="2"/></svg>
    <div class="footer__cols">
      <div class="footer__brand"><div class="brand"><span class="brand__dot"></span></div><div class="brand__name">Hearthway Homes</div><div class="footer__social"><i></i><i></i><i></i><i></i></div></div>
      <div class="footer__col"><h4>Company</h4><p>About us<br>How it works<br>Reviews<br>Careers</p></div>
      <div class="footer__col"><h4>Help</h4><p>FAQs<br>Contact<br>Privacy<br>Terms</p></div>
      <div class="footer__col"><h4>Contact</h4><p>0800 555 0192<br>hello@hearthwayhomes.com<br>Mon–Sat 8am–8pm</p></div>
    </div>
    <p class="footer__legal">© Hearthway Homes. All rights reserved.</p>
  </footer>

  <div class="overlay"></div>
  <div class="popup">
    <h3>Before you go – get your offer!</h3>
    <p>Leave your details and we will call you back</p>
    <div class="popup__field">First name</div>
    <div class="popup__field">Surname</div>
    <div class="popup__field">Email address</div>
    <div class="popup__field">Phone number</div>
    <div class="popup__field">Property address</div>
    <span class="btn">Submit</span>
  </div>
</main>

</body>
</html>
```